Dating Coach needs a Book Cover Design

My new book called "When to Turn the Tide: Meeting Romance Among the Endless Crowd of Digital Courtship" needs a cover! I tried to make one on my own, but it's just not my skill set :) Please see attached for my best attempt. I'd like to see the title smaller and the tagline bigger - so that the tagline is easier to read. But I'm not sure how to do this and still have the Title look great. I'm also considering if the "TURN THE TIDE" part should not be in all caps. Looking forward to your ideas! I'm also afraid that the drawing is a bit too cartoonish and doesn't match my brand. I'm looking for something elegant and also very approachable and down to earth. My website is www.petrawendtcoaching.example so you can use as reference! Please see my attached brand style guide for colors. This will be an e-book that I give away for free to anyone who signs up for my newsletter. Some mock-ups would also be great to use in advertising.

```html
<!DOCTYPE html>
<html lang="en">
<head>
<meta charset="utf-8">
<title>When to Turn the Tide — Book Cover</title>
<link rel="stylesheet" href="https://fonts.googleapis.com/css2?family=Cinzel:wght@500;600;700&family=Great+Vibes&family=Montserrat:wght@400&display=swap">
<style>
  :root {
    --backdrop: #5b5b5b;
    --cream-light: #fdf6e8;
    --cream-dark: #f1e5cc;
    --plum: #785684;
    --plum-deep: #5a3d64;
    --plum-text: #75548a;
    --gold: #c99b1c;
    --gold-light: #e6c04a;
    --white: #ffffff;
    --hay-light: #d9b46a;
    --hay-mid: #b98a3e;
    --heart-red: #c8242a;
    --ink: #333333;
  }
  * { margin: 0; padding: 0; box-sizing: border-box; }
  html, body {
    width: 1200px;
    height: 2948px;
    overflow: hidden;
    background: var(--backdrop);
  }
  .canvas {
    position: relative;
    width: 1200px;
    height: 2948px;
  }
  .book-cover {
    position: absolute;
    left: 150px;
    top: 1430px;
    width: 900px;
    height: 1347px;
    overflow: hidden;
    background: radial-gradient(ellipse at 50% 40%, var(--cream-light) 0%, var(--cream-light) 50%, var(--cream-dark) 100%);
    box-shadow: 16px 20px 36px rgba(0,0,0,0.45);
  }
  .cover-layer {
    position: absolute;
    left: 0;
    top: 0;
    width: 900px;
    height: 1347px;
  }
  .cover-text {
    position: absolute;
    left: 0;
    width: 100%;
    text-align: center;
    line-height: 1;
  }
  .kicker {
    top: 100px;
    height: 24px;
    font-family: "Montserrat", sans-serif;
    font-weight: 400;
    font-size: 23px;
    letter-spacing: 0.3em;
    color: var(--ink);
    display: flex;
    justify-content: center;
    align-items: center;
    gap: 14px;
  }
  .kicker::before, .kicker::after {
    content: "";
    display: block;
    width: 85px;
    height: 1.5px;
    background: var(--gold);
  }
  .script-title {
    top: 128px;
    font-family: "Great Vibes", cursive;
    font-size: 84px;
    line-height: 1.1;
    color: var(--gold);
  }
  .gold-rule {
    position: absolute;
    top: 238px;
    left: 210px;
    width: 484px;
    height: 1.5px;
    background: var(--gold);
  }
  .headline {
    top: 283px;
    font-family: "Cinzel", serif;
    font-weight: 700;
    font-size: 68px;
    color: var(--plum-text);
  }
  .heart-o {
    display: inline-block;
    width: 0.74em;
    height: 0.68em;
    vertical-align: -0.02em;
    margin: 0 0.02em;
  }
  .subhead {
    top: 354px;
    font-family: "Cinzel", serif;
    font-weight: 600;
    font-size: 52px;
    color: var(--plum-text);
  }
  .band-text {
    top: 492px;
    font-family: "Cinzel", serif;
    font-weight: 700;
    font-size: 70px;
    line-height: 60px;
    color: var(--white);
  }
  .author {
    top: 1254px;
    font-family: "Cinzel", serif;
    font-weight: 600;
    font-size: 36px;
    letter-spacing: 0.3em;
    color: var(--plum-text);
  }
</style>
</head>
<body>
<main class="canvas">
  <section class="book-cover">
    <svg class="cover-layer" viewBox="0 0 900 1347" role="img" aria-label="Photograph of a golden haystack with a small red heart resting on its peak">
      <defs>
        <radialGradient id="hayTone" cx="50%" cy="55%" r="55%">
          <stop offset="0%" stop-color="var(--hay-mid)" stop-opacity="0.85"/>
          <stop offset="55%" stop-color="var(--hay-light)" stop-opacity="0.55"/>
          <stop offset="100%" stop-color="var(--hay-light)" stop-opacity="0"/>
        </radialGradient>
        <radialGradient id="heartTone" cx="50%" cy="50%" r="50%">
          <stop offset="0%" stop-color="var(--heart-red)" stop-opacity="0.75"/>
          <stop offset="100%" stop-color="var(--heart-red)" stop-opacity="0"/>
        </radialGradient>
      </defs>
      <rect x="0" y="780" width="900" height="440" fill="url(#hayTone)"/>
      <rect x="450" y="810" width="100" height="100" fill="url(#heartTone)"/>
    </svg>

    <svg class="cover-layer" viewBox="0 0 900 1347" aria-hidden="true">
      <path fill="var(--plum-deep)" opacity="0.5"
        d="M0 438 L36 432 L66 444 L100 434 L140 441 L178 430 L214 443 L252 436 L284 425 L320 440 L358 432 L396 445 L440 434 L486 442 L524 428 L562 440 L604 432 L642 445 L680 433 L716 439 L752 426 L790 440 L834 432 L876 443 L900 433 L900 470 L0 470 Z"/>
      <path fill="var(--plum)"
        d="M0 446 L28 438 L58 450 L92 440 L130 447 L170 436 L210 449 L246 441 L278 431 L314 446 L352 438 L388 451 L430 440 L476 448 L514 434 L552 447 L592 438 L632 451 L670 439 L706 445 L742 433 L780 447 L824 438 L866 450 L900 438
           L900 712 L864 717 L832 705 L802 722 L764 713 L730 725 L698 714 L666 723 L630 711 L594 727 L558 717 L518 729 L486 716 L450 723 L414 713 L378 728 L342 718 L306 725 L270 712 L236 726 L200 717 L164 729 L126 718 L90 727 L56 715 L26 723 L0 715 Z"/>
    </svg>

    <p class="cover-text kicker">WHEN TO</p>
    <p class="cover-text script-title">Turn the Tide</p>
    <div class="gold-rule"></div>

    <h1 class="cover-text headline">MEETING R<svg class="heart-o" viewBox="0 0 32 29" role="img" aria-label="O"><defs><linearGradient id="goldHeart" x1="0" y1="0" x2="1" y2="1"><stop offset="0%" stop-color="var(--gold-light)"/><stop offset="100%" stop-color="var(--gold)"/></linearGradient></defs><path fill="url(#goldHeart)" d="M16 29 C6 21 0 15 0 8.5 C0 3.5 4 0 8.5 0 C12 0 14.6 2 16 4.6 C17.4 2 20 0 23.5 0 C28 0 32 3.5 32 8.5 C32 15 26 21 16 29 Z"/></svg>MANCE</h1>
    <p class="cover-text subhead">AMONG THE</p>

    <h2 class="cover-text band-text">ENDLESS CROWD<br>OF DIGITAL<br>COURTSHIP</h2>

    <p class="cover-text author">PETRA WENDT</p>
  </section>
</main>
</body>
</html>
```